Crestline Gas and Plumbing Business Card Design

I am after a business card design for my plumbing business called 'Crestline Gas & Plumbing'. I do all types of plumbing and gas work and specialise in general maintenance plumbing. Would like to see designs using current logo

Industry/Entity Type

Plumbing

Contact Information for Business Card

Name - Dale Whitcombe
Phone number - 0455163027
Email - admin@crestlinegasandplumbing.example.com.au
ABN - 68204915336

```html
<!DOCTYPE html>
<html lang="en">
<head>
<meta charset="utf-8">
<title>Crestline Gas &amp; Plumbing – Business Card</title>
<link href="https://fonts.googleapis.com/css2?family=Michroma&family=Exo+2:wght@400;500&display=swap" rel="stylesheet">
<style>
  :root {
    --backdrop: #2f2f31;
    --brand-blue: #2c3f9e;
    --brand-blue-deep: #2a3490;
    --brand-blue-light: #3d8fd8;
    --brand-orange: #e8891f;
    --card-white: #f7f7f7;
    --ink: #3a3a3a;
    --paper-edge: rgba(0,0,0,0.35);
  }
  * { box-sizing: border-box; margin: 0; padding: 0; }
  html, body { width: 1200px; height: 793px; overflow: hidden; }
  body {
    background: var(--backdrop);
    position: relative;
    font-family: "Exo 2", sans-serif;
  }
  .card {
    position: absolute;
    width: 520px;
    height: 297px;
    border-radius: 4px;
    box-shadow: 0 14px 30px var(--paper-edge);
    overflow: hidden;
  }
  .card-front {
    left: 90px; top: 90px;
    background: linear-gradient(135deg, #4b4fb0 0%, var(--brand-blue-light) 30%, var(--brand-blue) 60%, var(--brand-blue-deep) 100%);
  }
  .card-back {
    left: 590px; top: 405px;
    background: var(--card-white);
  }
  .wordmark {
    position: absolute;
    display: flex;
    align-items: center;
    gap: 12px;
    font-family: "Michroma", sans-serif;
    font-weight: 400;
    letter-spacing: 0.5px;
    white-space: nowrap;
  }
  .wordmark-dot {
    width: 22px; height: 22px;
    border-radius: 50%;
    background: var(--brand-orange);
    flex: none;
  }
  .card-front .wordmark {
    left: 62px; top: 130px;
    font-size: 20px;
    color: #ffffff;
  }
  .card-back .wordmark {
    left: 36px; top: 42px;
    font-size: 15px;
    color: var(--brand-blue);
  }
  .card-back .wordmark-dot { width: 16px; height: 16px; }
  .faint-mark {
    position: absolute;
    border-radius: 50%;
    background: rgba(255,255,255,0.06);
  }
  .card-front .faint-mark { width: 150px; height: 150px; right: 40px; top: 40px; }
  .card-back .faint-mark { width: 170px; height: 170px; right: 36px; top: 50px; background: rgba(0,0,0,0.04); }
  .contact {
    position: absolute;
    left: 116px; top: 116px;
    color: var(--ink);
  }
  .contact-name {
    font-family: "Michroma", sans-serif;
    font-size: 17px;
    color: var(--brand-blue);
    margin-bottom: 10px;
  }
  .contact-abn { font-size: 13px; margin-bottom: 4px; letter-spacing: 0.5px; }
  .contact-line {
    display: flex; align-items: center; gap: 8px;
    font-size: 12.5px; line-height: 19px; letter-spacing: 0.3px;
  }
  .contact-line svg { width: 12px; height: 12px; flex: none; }
</style>
</head>
<body>
  <section class="card card-front" aria-label="Card front">
    <div class="faint-mark"></div>
    <div class="wordmark"><span class="wordmark-dot"></span>Crestline Gas &amp; Plumbing</div>
  </section>

  <section class="card card-back" aria-label="Card back">
    <div class="faint-mark"></div>
    <div class="wordmark"><span class="wordmark-dot"></span>Crestline Gas &amp; Plumbing</div>
    <div class="contact">
      <p class="contact-name">DALE WHITCOMBE</p>
      <p class="contact-abn">ABN - 68204915336</p>
      <p class="contact-line">
        <svg viewBox="0 0 24 24" aria-hidden="true"><path fill="var(--brand-orange)" d="M6.6 10.8a15 15 0 0 0 6.6 6.6l2.2-2.2c.3-.3.7-.4 1-.2 1.1.4 2.3.6 3.6.6.6 0 1 .4 1 1V20c0 .6-.4 1-1 1A17 17 0 0 1 3 4c0-.6.4-1 1-1h3.5c.6 0 1 .4 1 1 0 1.3.2 2.5.6 3.6.1.3 0 .7-.2 1z"/></svg>
        0455163027
      </p>
      <p class="contact-line">
        <svg viewBox="0 0 24 24" aria-hidden="true"><path fill="var(--brand-orange)" d="M2 5h20v14H2z M2 5l10 8 10-8" stroke="#fff" stroke-width="1.5"/></svg>
        admin@crestlinegasandplumbing.example.com.au
      </p>
      <p class="contact-line">
        <svg viewBox="0 0 24 24" aria-hidden="true"><circle cx="12" cy="12" r="10" fill="var(--brand-orange)"/><path d="M2 12h20M12 2c3 3 3 17 0 20M12 2c-3 3-3 17 0 20" stroke="#fff" stroke-width="1.4" fill="none"/></svg>
        www.crestlinegasandplumbing.example.com.au
      </p>
    </div>
  </section>
</body>
</html>
```